Designing a brochures for an educational counseling service provider

We would like a 4 sided design on a 11x8.5 paper, half folded. I have including a sample design we did to give you an idea of what we envision but we welcome creativity to make beautiful looking flyers. Text for the flier is included as well as our logo.
- The most important thing is capturing our audience/market. We will be handing these flies to schools, organizations and individual clients.

www.plorvaeducationalconsultants.example

Target Market(s)

We are targeting international students wanting to study in the U.S and Canada.

Industry/Entity Type

Education

Requirements
Must have
• - Clean and clear
• - Our logo should visible and well placed.
• - Could you the pictures of students, libraries and school buildings or you could use the pictures we already have.
Nice to have
• We would like this to match business cards.

```html
<!DOCTYPE html>
<html lang="en">
<head>
<meta charset="utf-8">
<title>Plorva Educational Consultants – Brochure</title>
<link href="https://fonts.googleapis.com/css2?family=Lato:wght@400;700;900&family=Exo+2:wght@600;700&family=Oswald:wght@600&display=swap" rel="stylesheet">
<style>
  :root{
    --blue:#0a4fa0;
    --blue-deep:#062f78;
    --blue-bright:#1a73c8;
    --green:#6cc72c;
    --green-light:#9be04a;
    --ink:#1c2e5a;
    --paper:#ffffff;
    --bg:#e9ebee;
  }
  *{margin:0;padding:0;box-sizing:border-box}
  html,body{width:1200px;height:848px;overflow:hidden;background:var(--bg)}
  .spread{display:flex;width:1200px;height:848px}
  .panel{position:relative;width:600px;height:848px;background:var(--paper);overflow:hidden}
  .panel--back{border-right:1px solid #d8dbe0}
  .panel__art{position:absolute;inset:0;width:600px;height:848px}

  .brand{display:flex;align-items:center;gap:12px;position:absolute}
  .brand__dot{width:34px;height:34px;border-radius:50%;background:var(--green)}
  .brand__name{font-family:"Lato",sans-serif;font-weight:900;font-size:34px;letter-spacing:2px;color:var(--blue)}

  .about{position:absolute;left:50px;top:70px;width:500px;font-family:"Lato",sans-serif;color:var(--ink)}
  .about__title{font-weight:900;font-size:22px;color:var(--blue-bright);margin-bottom:8px;letter-spacing:.5px}
  .about__text{font-weight:700;font-size:14.5px;line-height:1.42;text-align:justify;margin-bottom:12px}
  .panel--back .brand{left:235px;top:420px}

  .contact{position:absolute;right:50px;top:505px;text-align:right;font-family:"Lato",sans-serif}
  .contact__call{font-weight:900;font-size:19px;color:var(--blue)}
  .contact__call span{color:var(--blue-bright)}
  .contact__email{font-size:11px;font-weight:700;color:var(--blue-bright);margin-top:4px}
  .contact__web{font-size:12.5px;font-weight:700;color:var(--blue);margin-top:2px}

  .panel--front .brand{left:140px;top:40px}
  .tagline{position:absolute;left:40px;right:30px;top:590px;text-align:center;color:#fff}
  .tagline__lead{font-family:"Exo 2",sans-serif;font-weight:700;font-size:27px;letter-spacing:1px}
  .tagline__accent{font-family:"Exo 2",sans-serif;font-weight:700;font-size:24px;color:var(--green-light);letter-spacing:.5px}
  .tagline__strong{font-family:"Oswald",sans-serif;font-weight:600;font-size:34px;line-height:1.15}
  .tagline__web{font-family:"Lato",sans-serif;font-weight:700;font-size:13px;letter-spacing:5px;margin-top:26px}
</style>
</head>
<body>
<main class="spread">

  <section class="panel panel--back">
    <svg class="panel__art" viewBox="0 0 600 848">
      <defs>
        <linearGradient id="backBlue" x1="0" y1="1" x2="1" y2="0">
          <stop offset="0" stop-color="#062f78"/><stop offset="1" stop-color="#1a73c8"/>
        </linearGradient>
        <radialGradient id="libraryTone" cx=".5" cy=".45" r=".6">
          <stop offset="0" stop-color="#c99a7c"/><stop offset=".6" stop-color="#7a4d3a"/><stop offset="1" stop-color="#3b2a26"/>
        </radialGradient>
      </defs>
      <path d="M0 848 L0 790 C240 815 470 710 600 520 L600 848 Z" fill="url(#backBlue)"/>
      <path d="M0 770 C230 800 460 700 600 500" fill="none" stroke="#6cc72c" stroke-width="14"/>
      <path d="M0 752 C230 782 455 690 600 485" fill="none" stroke="#9be04a" stroke-width="3"/>
      <circle cx="150" cy="690" r="150" fill="none" stroke="#0a4fa0" stroke-width="10" stroke-dasharray="520 1000" transform="rotate(-80 150 690)"/>
      <circle cx="150" cy="690" r="136" fill="url(#libraryTone)" role="img" aria-label="Photo of three students reading a book together in a library"/>
    </svg>

    <div class="about">
      <h2 class="about__title">ABOUT US:</h2>
      <p class="about__text">Our mission is to make quality education accessible and affordable to the families we serve. Our services are designed with the child's future in mind. Whether one is seeking an academic or non-academic environment, it is important to us that we set our clients up for success.</p>
      <p class="about__text">We are a family-centered organization and our goals are the same as those of our clients; for their child to thrive and reach their goals and dreams. With over 10 years of experience in the business, we are aware of the financial obstacles created by the ever increasing cost of education. Our expert consultants work closely with families to map out their educational budget and find the best affordable and quality educational options.</p>
    </div>

    <div class="brand"><span class="brand__dot"></span><span class="brand__name">PLORVA</span></div>

    <div class="contact">
      <p class="contact__call">CALL US: <span>555-014-2290</span></p>
      <p class="contact__email">Email: hello@plorvaeducationalconsultants.example</p>
      <p class="contact__web">www.plorvaeducationalconsultants.example</p>
    </div>
  </section>

  <section class="panel panel--front">
    <svg class="panel__art" viewBox="0 0 600 848">
      <defs>
        <linearGradient id="frontBlue" x1="0" y1="1" x2="1" y2="0">
          <stop offset="0" stop-color="#062f78"/><stop offset=".6" stop-color="#0a4fa0"/><stop offset="1" stop-color="#1a73c8"/>
        </linearGradient>
        <linearGradient id="studentsTone" x1="0" y1="0" x2="1" y2="1">
          <stop offset="0" stop-color="#6b4534"/><stop offset=".5" stop-color="#9a6a4e"/><stop offset="1" stop-color="#4a3028"/>
        </linearGradient>
      </defs>
      <path d="M280 158 C400 122 520 114 600 122" fill="none" stroke="#0a4fa0" stroke-width="8"/>
      <path d="M250 172 C390 132 520 126 600 134" fill="none" stroke="#6cc72c" stroke-width="4"/>
      <path d="M0 215 C150 160 400 138 600 150 L600 300 C460 455 250 505 70 478 C30 470 0 455 0 440 Z" fill="url(#studentsTone)" role="img" aria-label="Photo of three smiling students standing close together"/>
      <path d="M40 486 C230 530 460 455 600 305" fill="none" stroke="#6cc72c" stroke-width="8"/>
      <path d="M0 565 C210 600 460 500 600 335 L600 848 L0 848 Z" fill="url(#frontBlue)"/>
      <path d="M0 550 C215 585 455 485 600 322" fill="none" stroke="#6cc72c" stroke-width="12"/>
    </svg>

    <div class="brand"><span class="brand__dot"></span><span class="brand__name">PLORVA</span></div>

    <div class="tagline">
      <p class="tagline__lead">A full-service international</p>
      <p class="tagline__accent">educational consulting group serving</p>
      <p class="tagline__strong">students and families across the globe</p>
      <p class="tagline__web">www.plorvaeducationalconsultants.example</p>
    </div>
  </section>

</main>
</body>
</html>
```